WP website design (Harwick)

We need a wordpress design for an established auction and real estate company based in Florida. The winning design will incorporate a professional color scheme with company logo in a clean layout. The design needs to consider that this will be developed on a responsive theme. Colors are those that will highlight the logo.

Industry/Entity Type

Real Estate

Font styles to use
Serif
Sans Serif

Colors

Designer to choose colors to be used in the design.

Requirements
Must have
• Navigation:
1) Home
2) Auctions
3) Online Auctions
4) About Us
5) Services
6) Real Estate Listings
7) References
8) Contact Us

Colors will be blue (#000066) / red (#B10000) and black or other complementary color. Tagline to be used "Since 1977, Proven Results." Slideshow to be placed in the header or body of home page - please use stock real estate image.

Widgets: 1) Email Sign-up 2) Social media icons for FB and LinkedIn 3) Featured Listings 4) Testimonials 5) Register button

Footer will have smaller company logo, attached logos and contact info:
Phone: (555) 612-4408 Mobile: (555) 719-2263
Email: lorahartwick@mailvine.example
Address: 48 E. Marlow Avenue, Ste 317, Pensacola, FL 39815
Nice to have
• Use of a drop down menu:
Auctions-
1) Upcoming Auctions
2) Past Auctions

```html
<!DOCTYPE html>
<html lang="en">
<head>
<meta charset="utf-8">
<title>Harwick Auctions</title>
<link href="https://fonts.googleapis.com/css2?family=Noto+Serif:ital,wght@0,400;0,700;1,400;1,700&family=Open+Sans:wght@400;600&display=swap" rel="stylesheet">
<style>
:root{
  --navy:#2e3192;
  --navy-dark:#23266f;
  --red:#b10000;
  --price:#c40d0d;
  --page:#f0f0f0;
  --panel:#ffffff;
  --widget:#f2f2f2;
  --line:#dcdcdc;
  --text:#4a4a4a;
  --muted:#7b7b7b;
  --footer:#e4e4e4;
  --footer-bar:#d4d4d4;
  --serif:"Noto Serif", Georgia, serif;
  --sans:"Open Sans", Arial, sans-serif;
}
*{box-sizing:border-box;margin:0;padding:0}
html,body{width:1200px;height:2350px;overflow:hidden}
body{position:relative;background:var(--page);font-family:var(--serif);color:var(--text)}
.abs{position:absolute}

/* header */
.site-header{position:absolute;left:0;top:0;width:1200px;height:107px;background:#fff}
.brand{position:absolute;left:70px;top:22px;display:flex;align-items:center;gap:14px}
.brand-mark{width:58px;height:60px;background:var(--navy)}
.brand-name{font-family:var(--serif);font-weight:700;font-size:38px;color:var(--navy);letter-spacing:.5px}
.tagline{position:absolute;left:0;width:1200px;top:36px;text-align:center;font-style:italic;font-size:20px;color:var(--navy)}
.search{position:absolute;left:913px;top:36px;width:218px;height:34px;background:#4d86e0;display:flex;align-items:center}
.search span{font-family:var(--sans);font-style:italic;font-size:12px;color:#e6eeff;padding-left:10px;flex:1}
.search-btn{width:34px;height:34px;background:var(--navy-dark);display:flex;align-items:center;justify-content:center}

/* nav */
.main-nav{position:absolute;left:0;top:107px;width:1200px;height:40px;background:var(--navy)}
.main-nav ul{list-style:none;display:flex;position:absolute;left:70px;top:0;height:40px}
.main-nav li{height:40px;line-height:40px;font-size:17px;color:#fff;padding:0 20px}
.main-nav li.active{background:var(--red);font-weight:700;padding:0 22px}

/* hero */
.hero{position:absolute;left:0;top:147px;width:1200px;height:481px;
  background:linear-gradient(180deg,#7d8794 0%,#a9b0b8 28%,#8d9aa3 50%,#6a7a63 68%,#5b6a55 80%,#6f7f78 100%)}
.hero-caption{position:absolute;left:757px;top:219px;width:374px;height:138px;background:rgba(240,240,240,.88);padding:8px 20px}
.hero-caption h2{font-size:26px;font-weight:700;color:#1c1c1c;line-height:36px}
.hero-caption p{font-size:14px;color:#222;line-height:22px}
.hero-caption .price{font-size:26px;font-style:italic;font-weight:700;color:var(--price);margin-top:4px;line-height:30px}
.register-btn{position:absolute;left:1025px;top:357px;width:106px;height:32px;background:var(--navy);color:#fff;font-size:14px;font-weight:700;text-align:center;line-height:32px}

/* content */
.content{position:absolute;left:70px;top:628px;width:1061px;height:1432px;background:var(--panel);border-left:1px solid #e4e4e4;border-right:1px solid #e4e4e4}

.listing{position:absolute;left:91px;width:647px;height:254px;border:1px solid var(--line);background:#fff}
.listing-photo{position:absolute;left:17px;top:17px;width:257px;height:177px}
.listing-title{position:absolute;left:276px;top:17px;width:354px;height:42px;background:var(--navy);color:#fff;font-weight:700;font-size:20px;line-height:42px;padding-left:16px}
.listing-desc{position:absolute;left:292px;top:72px;width:322px;font-size:14px;line-height:22px;color:#444}
.listing-price{position:absolute;left:292px;top:144px;font-size:27px;font-style:italic;font-weight:700;color:var(--price)}
.listing-stats{position:absolute;left:0;top:209px;width:645px;height:43px;background:var(--widget);border-top:1px solid var(--line);display:flex}
.listing-stats div{flex:1;display:flex;align-items:center;justify-content:center;gap:8px;font-size:12.5px;color:#444;border-left:1px solid var(--line)}
.listing-stats div:first-child{border-left:none}

.pager{position:absolute;left:551px;top:2003px;display:flex;align-items:center;gap:6px;font-size:14px;color:#555}
.pager b{display:inline-block;width:28px;height:24px;line-height:22px;text-align:center;font-size:12px;font-weight:400;border:1px solid var(--line);color:#444}
.pager b.current{background:var(--navy);color:#fff;border-color:var(--navy)}
.pager .label{margin-right:6px}

/* sidebar */
.widget{position:absolute;left:775px;width:334px;background:var(--widget);box-shadow:0 10px 8px -8px rgba(0,0,0,.35)}
.widget-title{height:40px;background:var(--navy);color:#fff;font-size:22px;font-weight:400;line-height:40px;padding-left:16px}
.field{position:absolute;left:18px;width:297px;height:32px;background:#fff;border:1px solid #d2d2d2;display:flex;align-items:center;gap:8px;padding-left:8px;font-size:12px;color:#444}
.submit{position:absolute;left:18px;width:78px;height:32px;background:var(--navy);color:#fff;font-weight:700;font-size:14px;text-align:center;line-height:32px}

.avatar{position:absolute;left:19px;top:57px;width:94px;height:94px;border-radius:50%;background:radial-gradient(circle at 50% 40%,#8fb7de,#4b7fb8)}
.t-name{position:absolute;left:124px;top:62px;font-weight:700;color:var(--red);font-size:15px}
.t-role{position:absolute;left:124px;top:86px;font-size:12.5px;color:#666}
.t-date{position:absolute;left:124px;top:109px;font-size:12.5px;color:#222}
.t-text{position:absolute;left:25px;top:166px;width:290px;font-size:12.5px;line-height:23px;color:#666;text-align:justify}
.t-arrow{position:absolute;top:250px;width:24px;height:23px;display:flex;align-items:center;justify-content:center}

.video{position:absolute;left:775px;top:1238px;width:334px;height:213px;border:4px solid var(--navy);
  background:linear-gradient(180deg,#2a3542 0%,#3e4a55 45%,#4a3e38 65%,#2e3a28 100%)}

.news-item{position:absolute;left:18px;width:298px;height:86px;border-bottom:1px solid #dadada}
.news-date{position:absolute;left:0;top:0;width:74px;height:80px;border:1px solid #cfcfcf;background:#fff;text-align:center}
.news-date .m{height:34px;background:var(--navy);color:#fff;font-style:italic;font-weight:700;font-size:20px;line-height:34px}
.news-date .d{font-size:22px;color:#777;line-height:42px}
.news-head{position:absolute;left:87px;top:2px;font-weight:700;color:var(--red);font-size:15px}
.news-body{position:absolute;left:87px;top:26px;width:210px;font-size:12.5px;line-height:21px;color:#888}
.view-more{position:absolute;right:0;width:86px;height:25px;background:var(--navy);color:#fff;font-size:12px;font-weight:700;text-align:center;line-height:25px}

.social{position:absolute;top:58px;width:35px;height:35px;background:#8d8d8d}

/* footer */
.site-footer{position:absolute;left:0;top:2060px;width:1200px;height:235px;background:var(--footer)}
.footer-col{position:absolute;top:0;height:235px}
.footer-col h3{font-weight:400;font-size:19px;color:var(--red);padding-bottom:8px;border-bottom:1px solid #cacaca;margin-top:14px}
.footer-divider{position:absolute;top:0;width:1px;height:235px;background:#cfcfcf}
.footer-links{list-style:none;margin-top:10px}
.footer-links li{font-size:13px;line-height:24.5px;color:#222;display:flex;align-items:center;gap:9px}
.footer-links li::before{content:"";width:8px;height:8px;background:#333}
.footer-links li.active{color:var(--red)}
.footer-links li.active::before{background:var(--red)}
.about-text{font-size:13px;color:#222;margin-top:12px}
.badge{position:absolute;background:#9a9a9a}
.contact-row{position:absolute;left:0;display:flex;align-items:flex-start;gap:14px;font-size:13px;line-height:23px;color:#333}

.footer-bar{position:absolute;left:0;top:2295px;width:1200px;height:55px;background:var(--footer-bar);display:flex;align-items:center;justify-content:center;gap:22px}
.footer-brand{display:flex;align-items:center;gap:7px;font-weight:700;font-size:19px;color:var(--navy)}
.footer-brand i{display:block;width:26px;height:28px;background:var(--navy)}
.copyright{font-size:13px;color:#333}
</style>
</head>
<body>

<header class="site-header">
  <div class="brand"><span class="brand-mark"></span><span class="brand-name">Harwick</span></div>
  <p class="tagline">Since 1977, Proven Results.</p>
  <div class="search"><span>Search</span>
    <div class="search-btn"><svg width="16" height="16" viewBox="0 0 16 16"><circle cx="6.5" cy="6.5" r="4.8" fill="none" stroke="#fff" stroke-width="2"/><line x1="10" y1="10" x2="14.5" y2="14.5" stroke="#fff" stroke-width="2.4"/></svg></div>
  </div>
</header>

<nav class="main-nav">
  <ul>
    <li class="active">Home</li><li>About Us</li><li>Services</li><li>Online Auctions</li><li>Auctions</li><li>Real Estate Listing</li><li>References</li><li>Contact Us</li>
  </ul>
</nav>

<section class="hero" role="img" aria-label="City skyline of glass towers above a river and stone bridge under cloudy sky">
  <div class="hero-caption">
    <h2>Florida 5, Pinecrest, FL</h2>
    <p>Florida 5, Pinecrest, FL</p>
    <p>Nam liber tempor cum soluta nobis eleifend ...</p>
    <p class="price">$480,000</p>
  </div>
  <div class="register-btn">Regiter Now</div>
</section>

<main class="content"></main>

<!-- listings -->
<article class="listing" style="top:661px">
  <div class="listing-photo" role="img" aria-label="House exterior at dusk with lawn" style="background:linear-gradient(180deg,#3b4047 0%,#4c5156 50%,#3e5a34 80%,#2e4a26 100%)">
    <svg class="abs" style="left:110px;top:70px" width="36" height="36" viewBox="0 0 36 36"><circle cx="15" cy="15" r="11" fill="none" stroke="#fff" stroke-width="3"/><line x1="23" y1="23" x2="33" y2="33" stroke="#fff" stroke-width="4"/><line x1="10" y1="15" x2="20" y2="15" stroke="#fff" stroke-width="2.5"/><line x1="15" y1="10" x2="15" y2="20" stroke="#fff" stroke-width="2.5"/></svg>
  </div>
  <h3 class="listing-title">Florida 5, Pinecrest, FL</h3>
  <p class="listing-desc">Lorem ipsum dolor sit amet, cotetur adipiscing elit. Etiam laoreet justo arcu porttitor sapien cursus vitae.</p>
  <p class="listing-price">$480,000</p>
  <div class="listing-stats">
    <div><svg width="14" height="14"><rect x="1" y="1" width="12" height="12" fill="none" stroke="#222" stroke-width="2"/><circle cx="5" cy="5" r="1.3"/><circle cx="9" cy="9" r="1.3"/></svg>2200 sq ft</div>
    <div><svg width="20" height="12"><rect x="1" y="5" width="18" height="4" fill="#222"/><rect x="1" y="1" width="2" height="10" fill="#222"/><rect x="4" y="3" width="5" height="2" fill="#222"/></svg>2 Bedrooms</div>
    <div><svg width="20" height="14"><path d="M1 7h18v3a3 3 0 0 1-3 3H4a3 3 0 0 1-3-3z" fill="#222"/><rect x="3" y="1" width="2" height="6" fill="#222"/></svg>3 Bathrooms</div>
    <div><svg width="16" height="14"><path d="M1 6L8 1l7 5v7H1z" fill="none" stroke="#222" stroke-width="2"/><rect x="4" y="8" width="8" height="5" fill="#222"/></svg>2 Garages</div>
  </div>
</article>

<article class="listing" style="top:930px">
  <div class="listing-photo" role="img" aria-label="White suburban house with lawn under blue sky" style="background:linear-gradient(180deg,#4f8bd0 0%,#9cc1e6 35%,#d8d8d4 55%,#8a9a86 75%,#4f7f36 100%)"></div>
  <h3 class="listing-title">Florida 5, Pinecrest, FL</h3>
  <p class="listing-desc">Lorem ipsum dolor sit amet, cotetur adipiscing elit. Etiam laoreet justo arcu porttitor sapien cursus vitae.</p>
  <p class="listing-price">$750,000</p>
  <div class="listing-stats">
    <div><svg width="14" height="14"><rect x="1" y="1" width="12" height="12" fill="none" stroke="#222" stroke-width="2"/><circle cx="5" cy="5" r="1.3"/><circle cx="9" cy="9" r="1.3"/></svg>2200 sq ft</div>
    <div><svg width="20" height="12"><rect x="1" y="5" width="18" height="4" fill="#222"/><rect x="1" y="1" width="2" height="10" fill="#222"/><rect x="4" y="3" width="5" height="2" fill="#222"/></svg>2 Bedrooms</div>
    <div><svg width="20" height="14"><path d="M1 7h18v3a3 3 0 0 1-3 3H4a3 3 0 0 1-3-3z" fill="#222"/><rect x="3" y="1" width="2" height="6" fill="#222"/></svg>3 Bathrooms</div>
    <div><svg width="16" height="14"><path d="M1 6L8 1l7 5v7H1z" fill="none" stroke="#222" stroke-width="2"/><rect x="4" y="8" width="8" height="5" fill="#222"/></svg>2 Garages</div>
  </div>
</article>

<article class="listing" style="top:1200px">
  <div class="listing-photo" role="img" aria-label="Warm lit living room with cream sofas and shelving" style="background:linear-gradient(135deg,#5a3a24 0%,#8a6a4c 35%,#c9b89e 60%,#6e4a30 100%)"></div>
  <h3 class="listing-title">Florida 5, Pinecrest, FL</h3>
  <p class="listing-desc">Lorem ipsum dolor sit amet, cotetur adipiscing elit. Etiam laoreet justo arcu porttitor sapien cursus vitae.</p>
  <p class="listing-price">$520,000</p>
  <div class="listing-stats">
    <div><svg width="14" height="14"><rect x="1" y="1" width="12" height="12" fill="none" stroke="#222" stroke-width="2"/><circle cx="5" cy="5" r="1.3"/><circle cx="9" cy="9" r="1.3"/></svg>2200 sq ft</div>
    <div><svg width="20" height="12"><rect x="1" y="5" width="18" height="4" fill="#222"/><rect x="1" y="1" width="2" height="10" fill="#222"/><rect x="4" y="3" width="5" height="2" fill="#222"/></svg>2 Bedrooms</div>
    <div><svg width="20" height="14"><path d="M1 7h18v3a3 3 0 0 1-3 3H4a3 3 0 0 1-3-3z" fill="#222"/><rect x="3" y="1" width="2" height="6" fill="#222"/></svg>3 Bathrooms</div>
    <div><svg width="16" height="14"><path d="M1 6L8 1l7 5v7H1z" fill="none" stroke="#222" stroke-width="2"/><rect x="4" y="8" width="8" height="5" fill="#222"/></svg>2 Garages</div>
  </div>
</article>

<article class="listing" style="top:1469px">
  <div class="listing-photo" role="img" aria-label="Bedroom with dark wood bed and warm lamps" style="background:linear-gradient(160deg,#b89a76 0%,#8e6c4c 40%,#e8e2d8 60%,#3a281c 100%)"></div>
  <h3 class="listing-title">Florida 5, Pinecrest, FL</h3>
  <p class="listing-desc">Lorem ipsum dolor sit amet, cotetur adipiscing elit. Etiam laoreet justo arcu porttitor sapien cursus vitae.</p>
  <p class="listing-price">$170,000</p>
  <div class="listing-stats">
    <div><svg width="14" height="14"><rect x="1" y="1" width="12" height="12" fill="none" stroke="#222" stroke-width="2"/><circle cx="5" cy="5" r="1.3"/><circle cx="9" cy="9" r="1.3"/></svg>2200 sq ft</div>
    <div><svg width="20" height="12"><rect x="1" y="5" width="18" height="4" fill="#222"/><rect x="1" y="1" width="2" height="10" fill="#222"/><rect x="4" y="3" width="5" height="2" fill="#222"/></svg>2 Bedrooms</div>
    <div><svg width="20" height="14"><path d="M1 7h18v3a3 3 0 0 1-3 3H4a3 3 0 0 1-3-3z" fill="#222"/><rect x="3" y="1" width="2" height="6" fill="#222"/></svg>3 Bathrooms</div>
    <div><svg width="16" height="14"><path d="M1 6L8 1l7 5v7H1z" fill="none" stroke="#222" stroke-width="2"/><rect x="4" y="8" width="8" height="5" fill="#222"/></svg>2 Garages</div>
  </div>
</article>

<article class="listing" style="top:1739px">
  <div class="listing-photo" role="img" aria-label="Bright white bedroom with large window" style="background:linear-gradient(120deg,#3a3a3a 0%,#9aa0a6 30%,#e6e8ea 55%,#c8ccd0 100%)"></div>
  <h3 class="listing-title">Florida 5, Pinecrest, FL</h3>
  <p class="listing-desc">Lorem ipsum dolor sit amet, cotetur adipiscing elit. Etiam laoreet justo arcu porttitor sapien cursus vitae.</p>
  <p class="listing-price">$480,000</p>
  <div class="listing-stats">
    <div><svg width="14" height="14"><rect x="1" y="1" width="12" height="12" fill="none" stroke="#222" stroke-width="2"/><circle cx="5" cy="5" r="1.3"/><circle cx="9" cy="9" r="1.3"/></svg>2200 sq ft</div>
    <div><svg width="20" height="12"><rect x="1" y="5" width="18" height="4" fill="#222"/><rect x="1" y="1" width="2" height="10" fill="#222"/><rect x="4" y="3" width="5" height="2" fill="#222"/></svg>2 Bedrooms</div>
    <div><svg width="20" height="14"><path d="M1 7h18v3a3 3 0 0 1-3 3H4a3 3 0 0 1-3-3z" fill="#222"/><rect x="3" y="1" width="2" height="6" fill="#222"/></svg>3 Bathrooms</div>
    <div><svg width="16" height="14"><path d="M1 6L8 1l7 5v7H1z" fill="none" stroke="#222" stroke-width="2"/><rect x="4" y="8" width="8" height="5" fill="#222"/></svg>2 Garages</div>
  </div>
</article>

<div class="pager"><span class="label">Page 1 of 3</span><b class="current">01</b><b>02</b><b>03</b></div>

<!-- sidebar -->
<aside class="widget" style="top:661px;height:240px">
  <h2 class="widget-title">Email Signup</h2>
  <div class="field" style="top:52px"><svg width="14" height="14"><circle cx="7" cy="4.5" r="3.5" fill="#222"/><path d="M1 14a6 5 0 0 1 12 0z" fill="#222"/></svg>Name</div>
  <div class="field" style="top:94px"><svg width="16" height="12"><rect x="0.5" y="0.5" width="15" height="11" fill="#222"/><path d="M1 1l7 6 7-6" fill="none" stroke="#fff" stroke-width="1.4"/></svg>E-mail</div>
  <div class="field" style="top:136px"><svg width="12" height="14"><rect x="1" y="6" width="10" height="7" fill="#222"/><path d="M3 6V4a3 3 0 0 1 6 0v2" fill="none" stroke="#222" stroke-width="1.6"/></svg>Password</div>
  <div class="submit" style="top:187px">Submit</div>
</aside>

<aside class="widget" style="top:930px;height:276px">
  <h2 class="widget-title">Testimonials</h2>
  <div class="avatar" role="img" aria-label="Portrait of client in hard hat"></div>
  <p class="t-name">Dr.Lorem</p>
  <p class="t-role">(amet ahet dymmy text)</p>
  <p class="t-date">Posted on 12 Mar,2014</p>
  <p class="t-text">Lorem ipsum dolor sit amet, consectetur adipiscing elit. Proin interdum lobortis libero id convallis tincidunt massa.</p>
  <div class="t-arrow" style="left:0;background:#3b3b3b"><svg width="8" height="10"><path d="M6 1L2 5l4 4" fill="none" stroke="#fff" stroke-width="1.6"/></svg></div>
  <div class="t-arrow" style="right:0;background:var(--navy)"><svg width="8" height="10"><path d="M2 1l4 4-4 4" fill="none" stroke="#fff" stroke-width="1.6"/></svg></div>
</aside>

<div class="video" role="img" aria-label="Brick house at night, video preview">
  <svg class="abs" style="left:125px;top:67px" width="72" height="72" viewBox="0 0 72 72"><circle cx="36" cy="36" r="31" fill="none" stroke="#cfcfcf" stroke-width="6" opacity=".85"/><path d="M28 22l22 14-22 14z" fill="#cfcfcf" opacity=".9"/></svg>
</div>

<aside class="widget" style="top:1484px;height:380px">
  <h2 class="widget-title">Popular news</h2>
  <div class="news-item" style="top:56px">
    <div class="news-date"><div class="m">Mar</div><div class="d">11</div></div>
    <p class="news-head">Lorem ipsum dolor sit</p>
    <p class="news-body">Lorem ipsum dolor sit amet, cosectur adipiscing elit.</p>
  </div>
  <div class="news-item" style="top:163px">
    <div class="news-date"><div class="m">Jan</div><div class="d">05</div></div>
    <p class="news-head">Lorem ipsum dolor sit</p>
    <p class="news-body">Lorem ipsum dolor sit amet, cosecetur adipiscing elit.</p>
  </div>
  <div class="news-item" style="top:271px;border-bottom:none">
    <div class="news-date"><div class="m">Jan</div><div class="d">07</div></div>
    <p class="news-head">Lorem ipsum dolor sit</p>
    <p class="news-body">Lorem ipsum dolor sit amet, cosecetur adipiscing elit.</p>
  </div>
  <div class="view-more" style="top:355px">View more</div>
</aside>

<aside class="widget" style="top:1897px;height:121px">
  <h2 class="widget-title">Followers</h2>
  <span class="social" style="left:18px;background:#3f5a94" role="img" aria-label="Social profile"></span>
  <span class="social" style="left:71px" role="img" aria-label="Social profile"></span>
  <span class="social" style="left:124px" role="img" aria-label="Social profile"></span>
  <span class="social" style="left:176px" role="img" aria-label="Social profile"></span>
  <span class="social" style="left:229px" role="img" aria-label="Social profile"></span>
  <span class="social" style="left:282px" role="img" aria-label="News feed"></span>
</aside>

<!-- footer -->
<footer class="site-footer">
  <div class="footer-col" style="left:86px;width:170px">
    <h3>Harwick</h3>
    <ul class="footer-links">
      <li class="active">Home</li><li>About Us</li><li>online Auctions</li><li>Service</li><li>Real Estate Listing</li><li>References</li><li>Contact Us</li>
    </ul>
  </div>
  <span class="footer-divider" style="left:279px"></span>
  <div class="footer-col" style="left:357px;width:336px">
    <h3>About Harwick</h3>
    <p class="about-text">Lorem ipsum dolor sit amet, consectetur adipiscing</p>
    <span class="badge" style="left:0;top:99px;width:40px;height:50px" role="img" aria-label="Partner association badge"></span>
    <span class="badge" style="left:48px;top:109px;width:70px;height:30px;background:#b4b4b4" role="img" aria-label="Partner association badge"></span>
    <span class="badge" style="left:130px;top:99px;width:68px;height:52px;background:#a8a8a8" role="img" aria-label="State association badge"></span>
    <span class="badge" style="left:250px;top:104px;width:50px;height:40px;background:#b8b8b8" role="img" aria-label="State realtors badge"></span>
    <span class="badge" style="left:0;top:177px;width:36px;height:40px;background:#555" role="img" aria-label="Certification badge"></span>
    <span class="badge" style="left:42px;top:185px;width:100px;height:24px;background:#b0b0b0" role="img" aria-label="Certification badge"></span>
    <span class="badge" style="left:145px;top:183px;width:125px;height:28px;background:#a4a4a4" role="img" aria-label="Local association badge"></span>
    <span class="badge" style="left:293px;top:165px;width:44px;height:58px;background:#333" role="img" aria-label="Auctioneers association badge"></span>
  </div>
  <span class="footer-divider" style="left:774px"></span>
  <div class="footer-col" style="left:851px;width:260px">
    <h3>Contact Us</h3>
    <div class="contact-row" style="top:66px"><svg width="16" height="24" viewBox="0 0 16 24"><path d="M8 1a7 7 0 0 0-7 7c0 6 7 15 7 15s7-9 7-15a7 7 0 0 0-7-7z" fill="#333"/><circle cx="8" cy="8" r="2.6" fill="#e4e4e4"/></svg><span>48 E. Marlow Avenue, Ste 317,<br>Pensacola, FL 39815</span></div>
    <div class="contact-row" style="top:129px;align-items:center;gap:8px"><svg width="16" height="16" viewBox="0 0 16 16"><path d="M3 1l3 3-2 2c1 2 3 4 6 6l2-2 3 3-2 2C7 15 1 9 1 3z" fill="#333"/></svg><span>(555) 612-4408</span><svg style="margin-left:4px" width="10" height="16"><rect x="1" y="1" width="8" height="14" rx="1.5" fill="#333"/><rect x="2.5" y="3" width="5" height="8" fill="#e4e4e4"/></svg><span>: (555) 719-2263</span></div>
    <div class="contact-row" style="top:174px;align-items:center"><svg width="18" height="14" viewBox="0 0 18 14"><path d="M1 5l8-4 8 4v8H1z" fill="#333"/><path d="M2 5l7 4 7-4" fill="none" stroke="#e4e4e4" stroke-width="1.3"/></svg><span>lorahartwick@mailvine.example</span></div>
  </div>
</footer>

<div class="footer-bar">
  <div class="footer-brand"><i></i>Harwick</div>
  <p class="copyright">Copyright © 2014 by harwick. All Rights Reserved</p>
</div>

</body>
</html>
```